Bruntel general construction

We need an website that are similar to these websites:
https://www.morvexa.com/en/
https://dulnari.com/company/

but with a tweak. Do not copy the entire website but atleast similar and yet better than them.

For reference this our current website.
https://bruntel.ph/

For the winning Designer please help us with the migration from our old website to the new redesign website.

```html
<!DOCTYPE html>
<html lang="en">
<head>
<meta charset="utf-8">
<title>Bruntel — Engineering the Infrastructure the Philippines Runs On</title>
<link href="https://fonts.googleapis.com/css2?family=Barlow+Condensed:wght@500;600&family=IBM+Plex+Sans:wght@400;500;600;700&display=swap" rel="stylesheet">
<style>
:root{
  --ink:#16191c;
  --panel:#15181b;
  --orange:#e85a12;
  --white:#ffffff;
  --text:#3c4248;
  --muted:#5f666d;
  --line:#d9dcdf;
  --footer:#275a78;
  --cond:"Barlow Condensed", sans-serif;
  --sans:"IBM Plex Sans", sans-serif;
}
*{box-sizing:border-box;margin:0;padding:0}
html,body{width:1200px;height:3193px;overflow:hidden}
body{position:relative;font-family:var(--sans);color:var(--text);background:#fff}
a{color:inherit;text-decoration:none}

/* hero */
.hero{position:absolute;left:0;top:0;width:1200px;height:926px;overflow:hidden;
  background:radial-gradient(ellipse at 60% 30%,#6b4536 0%,#3b2722 35%,#120d0c 70%,#050505 100%)}
.hero-photo{position:absolute;inset:0;background:linear-gradient(180deg,rgba(0,0,0,0) 40%,rgba(0,0,0,.85) 80%,#000 100%)}
.brand{position:absolute;font-family:var(--sans);font-weight:700;color:#fff;letter-spacing:.02em;display:flex;align-items:center;gap:8px}
.brand .dot{width:14px;height:14px;border-radius:50%;background:#fff}
.nav{position:absolute;left:421px;top:58px;display:flex;gap:31px;font-family:var(--cond);font-weight:600;font-size:17px;color:#fff;letter-spacing:.03em}
.btn{position:absolute;display:flex;align-items:center;justify-content:center;font-family:var(--cond);font-weight:600;font-size:17px;letter-spacing:.03em;color:#fff}
.btn-orange{background:var(--orange)}
.btn-ghost{border:1px solid rgba(255,255,255,.7)}
.eyebrow-hero{position:absolute;left:124px;top:322px;display:flex;align-items:center;gap:12px;font-size:13px;font-weight:500;color:#fff;letter-spacing:.04em}
.eyebrow-hero::before{content:"";width:80px;height:2px;background:#fff}
.hero h1{position:absolute;left:124px;top:350px;font-family:var(--sans);font-weight:700;font-size:51px;line-height:66px;color:#fff;letter-spacing:.01em}
.hero h1 em{font-style:normal;color:var(--orange)}
.hero .lede{position:absolute;left:124px;top:560px;width:595px;font-size:16px;line-height:24px;color:#e6e6e6;letter-spacing:.01em}
.hero .rule{position:absolute;left:124px;top:749px;width:950px;height:1px;background:rgba(255,255,255,.35)}
.stat{position:absolute;top:790px;color:#fff}
.stat b{display:block;font-weight:500;font-size:42px;line-height:50px}
.stat span{display:block;margin-top:8px;font-size:13.5px;line-height:21px;color:#d8d8d8;letter-spacing:.02em}

/* section heads */
.eyebrow{position:absolute;left:124px;font-size:13px;font-weight:500;color:var(--orange);letter-spacing:.06em}
.title{position:absolute;left:124px;font-weight:600;font-size:24px;color:var(--ink);letter-spacing:.01em}
.link-all{position:absolute;right:126px;top:1043px;font-size:13px;font-weight:500;color:var(--ink);text-decoration:underline;letter-spacing:.05em}

/* sector grid */
.sectors{position:absolute;left:124px;top:1106px;width:950px;height:582px;display:grid;grid-template-columns:316px 319px 315px;grid-template-rows:291px 291px;border:1px solid var(--line)}
.card{position:relative;border-right:1px solid var(--line);border-bottom:1px solid var(--line);padding:0 19px}
.card:nth-child(3n){border-right:0}
.card:nth-child(n+4){border-bottom:0}
.icon{position:absolute;left:19px;top:37px;width:84px;height:84px;border-radius:50%;background:#111}
.card h3{position:absolute;left:19px;top:156px;font-family:var(--cond);font-weight:600;font-size:24px;letter-spacing:.06em;color:var(--ink)}
.card p{position:absolute;left:19px;top:197px;width:275px;font-size:11.5px;line-height:19px;color:var(--muted);letter-spacing:.02em}
.card.cta{background:var(--panel)}
.card.cta h3{top:34px;color:#fff}
.card.cta p{top:76px;width:225px;color:#c9cdd0}
.card.cta .btn{left:19px;top:203px;width:138px;height:49px}

/* process */
.process{position:absolute;left:0;top:1731px;width:1200px;height:481px;
  background:linear-gradient(180deg,#202020 0%,#2c2c2c 45%,#1c1c1c 100%)}
.process .title{color:#fff}
.stages{position:absolute;left:124px;top:193px;width:950px;height:217px;border-top:1px solid rgba(255,255,255,.35);border-bottom:1px solid rgba(255,255,255,.35)}
.stage{position:absolute;top:0;height:217px;padding-left:19px;border-left:1px solid rgba(255,255,255,.35)}
.stage:first-child{border-left:0}
.stage .num{position:absolute;top:33px;left:19px;font-family:var(--cond);font-weight:600;font-size:24px;color:var(--orange);letter-spacing:.05em}
.stage h4{position:absolute;top:82px;left:19px;font-family:var(--cond);font-weight:600;font-size:24px;color:#fff;letter-spacing:.07em}
.stage p{position:absolute;top:123px;left:19px;width:185px;font-size:13px;line-height:19px;color:#c7c7c7;letter-spacing:.02em}

/* news */
.tile{position:absolute;overflow:hidden}
.tile .caption{position:absolute;left:22px;bottom:20px;right:50px;color:#fff;font-weight:600;font-size:12px;line-height:22px}
.tile.big .caption{left:25px;right:190px;font-size:15px;line-height:22px}

/* footer */
.footer{position:absolute;left:0;top:2933px;width:1200px;height:260px;background:var(--footer);color:#fff}
.footer .about{position:absolute;left:124px;top:149px;width:260px;font-size:10px;line-height:18px;color:#e4edf2}
.fcol{position:absolute;top:52px}
.fcol h5{font-weight:500;font-size:13px;margin-bottom:16px}
.fcol a{display:block;font-size:10px;line-height:22px;color:#e4edf2}
</style>
</head>
<body>

<header class="hero">
  <div class="hero-photo" role="img" aria-label="Low-angle photo of tall industrial chimney stacks under a smoky sky"></div>
  <a class="brand" href="https://bruntel.ph/" style="left:124px;top:56px;font-size:20px"><span class="dot"></span>BRUNTEL</a>
  <nav class="nav"><a href="#sectors">SECTORS</a><a href="#capability">CAPABILITY</a><a href="#track">TRACK RECORD</a><a href="#contact">CONTACT</a></nav>
  <a class="btn btn-orange" href="#contact" style="left:945px;top:45px;width:129px;height:49px">START A PROJECT</a>

  <div class="eyebrow-hero">BRUNTEL INC — CAVITE, PHILIPPINES</div>
  <h1>ENGINEERING THE<br>INFRASTRUCTURE <em>THE</em><br><em>PHILIPPINES RUNS ON</em></h1>
  <p class="lede">Power, water, environmental and civil works, delivered by one in-house team<br>—from feasibility through decades of maintenance.</p>
  <a class="btn btn-orange" href="#sectors" style="left:124px;top:650px;width:137px;height:49px">VIEW SECTORS →</a>
  <a class="btn btn-ghost" href="#track" style="left:276px;top:650px;width:138px;height:49px">TRACK RECORD</a>

  <div class="rule"></div>
  <div class="stat" style="left:124px"><b>30+</b><span>Years Delivering Industrial<br>Infrastructure</span></div>
  <div class="stat" style="left:392px"><b>120+</b><span>Projects Completed Across<br>Five Sectors</span></div>
  <div class="stat" style="left:661px"><b>850</b><span>Multi-Skilled Technical<br>Personnel</span></div>
  <div class="stat" style="left:901px"><b>24/7</b><span>Site Coverage on Active<br>Contracts</span></div>
</header>

<section id="sectors">
  <p class="eyebrow" style="top:1003px">WHAT WE BUILD AND MAINTAIN</p>
  <h2 class="title" style="top:1033px">FIVE SECTORS, ONE ACCOUNTABLE TEAM</h2>
  <a class="link-all" href="#capability">FULL CAPABILITY LIST</a>

  <div class="sectors">
    <article class="card"><div class="icon" role="img" aria-label="Power generation icon: shield with a seedling"></div><h3>POWER GENERATION</h3><p>Refurbishment, repair, maintenance, and shutdown solutions for utility and steam-generating facilities—from valves and pumps to turbines and critical rotating equipment.</p></article>
    <article class="card"><div class="icon" role="img" aria-label="Water treatment icon: cooling towers over water"></div><h3>WATER TREATMENT</h3><p style="width:230px">Design, construction, and maintenance of water and wastewater treatment systems, desalination facilities, and sustainable utility infrastructure.</p></article>
    <article class="card"><div class="icon" role="img" aria-label="Construction icon: drilling rig"></div><h3>CONSTRUCTION</h3><p>Refurbishment, repair, maintenance, and shutdown solutions for utility and steam-generating facilities—from valves and pumps to turbines and critical rotating equipment.</p></article>
    <article class="card"><div class="icon" role="img" aria-label="Oil and gas icon: droplets" style="left:25px;width:72px;height:72px;top:43px"></div><h3>OIL &amp; GAS</h3><p>Refurbishment, repair, maintenance, and shutdown solutions for utility and steam-generating facilities—from valves and pumps to turbines and critical rotating equipment.</p></article>
    <article class="card"><div class="icon" role="img" aria-label="Environmental protection icon: crane truck"></div><h3>ENVIRONMENTAL PROTECTION</h3><p>Refurbishment, repair, maintenance, and shutdown solutions for utility and steam-generating facilities—from valves and pumps to turbines and critical rotating equipment.</p></article>
    <article class="card cta"><h3>SCOPE A PROJECT</h3><p>Refurbishment, repair, maintenance, and shutdown solutions for utility and steam-generating facilities—from valves and pumps to turbines and critical rotating equipment.</p><a class="btn btn-orange" href="#contact">TALK TO US →</a></article>
  </div>
</section>

<section class="process" id="capability" role="img" aria-label="Dark background photo of construction cranes">
  <p class="eyebrow" style="top:95px">HOW A CONTRACT RUNS</p>
  <h2 class="title" style="top:126px">FOUR STAGES, ONE TEAM THROUGHOUT</h2>
  <div class="stages">
    <div class="stage" style="left:0;width:222px"><span class="num">01</span><h4>ASSESS</h4><p>We begin with detailed site surveys, feasibility studies, engineering evaluations, and HSE risk assessments.</p></div>
    <div class="stage" style="left:222px;width:245px"><span class="num">02</span><h4>BUILD</h4><p>Our in-house engineering teams execute construction and installation with strict quality control.</p></div>
    <div class="stage" style="left:467px;width:233px"><span class="num">03</span><h4>COMMISSION</h4><p>Comprehensive testing, system validation, performance verification, and complete documentation.</p></div>
    <div class="stage" style="left:700px;width:250px"><span class="num">04</span><h4>MAINTAIN</h4><p>Long-term maintenance, inspections, shutdown support, asset integrity management, and rapid.</p></div>
  </div>
</section>

<section id="track">
  <p class="eyebrow" style="top:2281px">WHAT WE BUILD AND MAINTAIN</p>
  <h2 class="title" style="top:2311px">FIVE SECTORS, ONE ACCOUNTABLE TEAM</h2>

  <a class="tile big" href="#" style="left:125px;top:2385px;width:522px;height:506px;background:linear-gradient(180deg,#cfd3d2 0%,#aeb5b1 45%,#5f7446 70%,#3d5a2c 100%)" role="img" aria-label="Photo of an oil pumpjack in a green field">
    <span class="caption">Environmental Protection Industry A Job Creator</span>
  </a>
  <a class="tile" href="#" style="left:668px;top:2385px;width:406px;height:243px;background:linear-gradient(180deg,#4a5566 0%,#3a3f48 50%,#1c1f24 100%)" role="img" aria-label="Photo of an offshore rig at dusk">
    <span class="caption">Hydraxa To Supply Turbocharger Technology for Saudi Desalination Projects</span>
  </a>
  <a class="tile" href="#" style="left:668px;top:2649px;width:406px;height:242px;background:linear-gradient(90deg,#9a9a9a 0%,#6d6d6d 50%,#3a3a3a 100%)" role="img" aria-label="Black and white photo of a refinery with steam">
    <span class="caption">Positive Signs for Oilfield Services Sector as U.S. Onshore Market Set to Grow</span>
  </a>
</section>

<footer class="footer" id="contact">
  <a class="brand" href="https://bruntel.ph/" style="left:124px;top:76px;font-size:15px"><span class="dot" style="width:11px;height:11px"></span>BRUNTEL</a>
  <p class="about">We assist in the advancement of an environmental friendly society by providing our services to world-renowned environmental EPC companies.</p>
  <div class="fcol" style="left:433px"><h5>Quick Links</h5><a href="#">Companies</a><a href="#">Projects</a><a href="#">Tenders</a><a href="#">Market Data</a><a href="#">Suppliers</a></div>
  <div class="fcol" style="left:615px"><h5>Information</h5><a href="#">Waste Types</a><a href="#">Environmental Policy</a><a href="#">Terms &amp; Conditions</a><a href="#">Privacy Policy</a><a href="#">Sitemap</a></div>
  <div class="fcol" style="left:820px"><h5>Contact Us</h5><a href="tel:+639175550142">Call: +63 917 555 0142</a><a href="mailto:hello@bruntel.ph">Mail: hello@bruntel.ph</a></div>
</footer>

</body>
</html>
```